I need a business card for myself, being a proprietor of a funeral parlor based in Manila. I'd like the card to have either of the following:
White Font on Black Background
or
Black Font on White Background
No logo is needed however I will appreciate any efforts to show a symbol of eternal happiness, aptly designed with above mentioned colors in mind.
Company name, address and contact on the lower right corner.
Logo or symbol anywhere.
Quillstone Funeral Services
+639174826351
darvik4521@pelmora.com
corner of Brisco Avenue and Velhurst Street
Makati City, Philippines
Thank you.
Update: Please include a small dove in your design. You are free to choose where you would like it on the card.

```html
<!DOCTYPE html>
<html lang="en">
<head>
<meta charset="utf-8">
<title>Quillstone Funeral Services – Business Card</title>
<link rel="stylesheet" href="https://fonts.googleapis.com/css2?family=Open+Sans:wght@400;600;700&display=swap">
<style>
  :root {
    --page-bg: #ffffff;
    --front-center: #5e5e5e;
    --front-mid: #2b2b2b;
    --front-edge: #111111;
    --back-center: #c9c9cc;
    --back-mid: #7a7a7c;
    --back-edge: #0c0c0c;
    --ink-light: #ffffff;
    --ink-dark: #141414;
  }
  * { margin: 0; padding: 0; box-sizing: border-box; }
  html, body {
    width: 1200px;
    height: 1000px;
    overflow: hidden;
    background: var(--page-bg);
    font-family: "Open Sans", Arial, sans-serif;
  }
  .sheet { position: relative; width: 1200px; height: 1000px; }
  .card {
    position: absolute;
    width: 504px;
    height: 296px;
  }
  .card-front {
    left: 89px;
    top: 185px;
    background: radial-gradient(ellipse 300px 220px at 350px 100px,
      var(--front-center) 0%, var(--front-mid) 55%, var(--front-edge) 100%);
    color: var(--ink-light);
  }
  .card-back {
    left: 528px;
    top: 624px;
    background: radial-gradient(ellipse 330px 230px at 252px 170px,
      var(--back-center) 0%, var(--back-mid) 60%, var(--back-edge) 100%);
    color: var(--ink-dark);
  }
  .brand {
    position: absolute;
    text-align: center;
    line-height: 1;
  }
  .brand-name { display: block; font-size: 40px; font-weight: 600; letter-spacing: 0.5px; }
  .brand-tag { display: block; font-size: 17px; font-weight: 700; margin-top: 12px; letter-spacing: 0.4px; }
  .brand-mark {
    position: absolute;
    width: 16px;
    height: 16px;
    border-radius: 50%;
    background: var(--ink-light);
  }
  .card-front .brand { left: 242px; top: 62px; width: 210px; }
  .card-front .brand-mark { left: 440px; top: 46px; }
  .card-back .brand { left: 147px; top: 122px; width: 210px; }
  .card-back .brand-mark { left: 336px; top: 104px; }
  .contact {
    position: absolute;
    left: 38px;
    top: 172px;
    font-size: 15px;
    line-height: 24px;
    letter-spacing: 0.8px;
    list-style: none;
  }
</style>
</head>
<body>
  <main class="sheet">
    <section class="card card-front" aria-label="Card front">
      <span class="brand-mark" aria-hidden="true"></span>
      <div class="brand">
        <span class="brand-name">Quillstone</span>
        <span class="brand-tag">FUNERAL SERVICES</span>
      </div>
      <ul class="contact">
        <li>+639174826351</li>
        <li>darvik4521@pelmora.com</li>
        <li>corner of Brisco Avenue and Velhurst Street</li>
        <li>Makati City, Philippines</li>
      </ul>
    </section>
    <section class="card card-back" aria-label="Card back">
      <span class="brand-mark" aria-hidden="true"></span>
      <div class="brand">
        <span class="brand-name">Quillstone</span>
        <span class="brand-tag">FUNERAL SERVICES</span>
      </div>
    </section>
  </main>
</body>
</html>
```